Real Estate For Sale Sign

I need to design a for sale sign. It needs to include The following information
Logo: Attached
Name: Corinne Vasquel,
Company Name: Gilded Harbor Real Estate,
Phone Number: 503-841-2096
BRE Licence Number 04817359 (Can Be small)
Sign size 24x30

I am not sure about including my website but I would like to see options with it. www.gildedharbor-example.com
Updates

Target Market(s)

Potential Buyers or Sellers of Real Estate. Must be easy to read.

Industry/Entity Type

Real Estate

Requirements
Must have
• I want it to feel luxurious and sharp.

```html
<!DOCTYPE html>
<html lang="en">
<head>
<meta charset="utf-8">
<title>Gilded Harbor Real Estate – For Sale Sign 24 x 30</title>
<link href="https://fonts.googleapis.com/css2?family=Cinzel:wght@400;600&family=Open+Sans:wght@400;600&display=swap" rel="stylesheet">
<style>
  :root {
    --page-bg: #e4e5e7;
    --bar-sky: #00bfff;
    --bar-azure: #0099ff;
    --bar-ocean: #006699;
    --bar-indigo: #4a4f7a;
    --bar-slate: #7d8299;
    --panel-top: #9aa1a8;
    --panel-mid: #dfe8f0;
    --panel-low: #c9d3dc;
    --panel-base: #38424d;
    --brand-blue: #2a5fa6;
    --brand-grey: #7d7f85;
    --phone-ink: #2b2b2d;
    --rule: #9aa3ad;
    --licence-ink: #f2f4f6;
  }
  * { margin: 0; padding: 0; box-sizing: border-box; }
  html, body {
    width: 1200px; height: 1000px; overflow: hidden;
    background: var(--page-bg);
  }
  .sign {
    position: absolute; left: 150px; top: 140px;
    width: 900px; height: 720px;
    background:
      linear-gradient(180deg,
        var(--panel-top) 0%,
        var(--panel-mid) 40%,
        var(--panel-mid) 52%,
        #a9b1b9 66%,
        var(--panel-low) 68%,
        var(--panel-mid) 78%,
        #9aa4ae 90%,
        var(--panel-base) 100%);
    box-shadow: 6px 8px 14px rgba(0,0,0,.28);
    overflow: hidden;
  }
  .colour-bar { display: flex; height: 37px; }
  .colour-bar span { display: block; height: 100%; }
  .colour-bar .sky { width: 31.6%; background: var(--bar-sky); }
  .colour-bar .azure { width: 29.4%; background: var(--bar-azure); }
  .colour-bar .ocean { width: 23.3%; background: var(--bar-ocean); }
  .colour-bar .indigo { width: 4.6%; background: var(--bar-indigo); }
  .colour-bar .slate { width: 11.1%; background: var(--bar-slate); }

  .brand-mark { position: absolute; left: 38px; top: 202px; }
  .brand-name {
    position: absolute; left: 325px; top: 268px;
    font-family: 'Cinzel', serif; font-weight: 600;
    color: var(--brand-blue); text-align: center;
  }
  .brand-name .primary { display: block; font-size: 64px; line-height: 1; letter-spacing: 1px; }
  .brand-name .secondary { display: block; font-size: 27px; letter-spacing: 10px; margin-top: 16px; }

  .agent {
    position: absolute; right: 42px; top: 552px;
    text-align: right;
  }
  .agent-name {
    font-family: 'Cinzel', serif; font-weight: 400;
    font-size: 34px; line-height: 1; letter-spacing: .5px;
  }
  .agent-name .first { color: var(--brand-blue); }
  .agent-name .last { color: var(--brand-grey); }
  .agent-phone {
    font-family: 'Open Sans', sans-serif; font-weight: 600;
    font-size: 43px; line-height: 1; color: var(--phone-ink);
    margin-top: 14px; letter-spacing: .5px;
  }
  .agent-licence {
    font-family: 'Open Sans', sans-serif; font-weight: 400;
    font-size: 14.5px; letter-spacing: 2px; color: var(--licence-ink);
    border-top: 1px solid var(--rule);
    margin-top: 7px; padding-top: 5px;
  }
</style>
</head>
<body>
  <main class="sign">
    <div class="colour-bar">
      <span class="sky"></span><span class="azure"></span><span class="ocean"></span><span class="indigo"></span><span class="slate"></span>
    </div>

    <svg class="brand-mark" width="240" height="240" viewBox="0 0 240 240" aria-hidden="true">
      <circle cx="120" cy="120" r="112" fill="none" stroke="var(--bar-azure)" stroke-width="5"/>
    </svg>

    <h1 class="brand-name">
      <span class="primary">GILDED HARBOR</span>
      <span class="secondary">REAL ESTATE</span>
    </h1>

    <section class="agent">
      <p class="agent-name"><span class="first">CORINNE</span> <span class="last">VASQUEL</span></p>
      <p class="agent-phone">503-841-2096</p>
      <p class="agent-licence">BRE LICENCE NUMBER 04817359</p>
    </section>
  </main>
</body>
</html>
```